Maplecrest Ambulatory Flyer

Need to make a flyer similar to the attached Tri Vale pdfs for Maplecrest Ambulatory. The write up is attached or can be found at https://www.medivantasc.com/bronx

Requirements
Must have
• What the existing flyer has.

```html
<!DOCTYPE html>
<html lang="en">
<head>
<meta charset="utf-8">
<title>Maplecrest Ambulatory Surgery Center Flyer</title>
<link rel="stylesheet" href="https://fonts.googleapis.com/css2?family=Montserrat:wght@600&family=Questrial&family=Playfair+Display+SC:wght@700&display=swap">
<style>
:root{
  --blue:#4474b4;
  --blue-dark:#2f5f9f;
  --ink:#1d1d1f;
  --paper:#ffffff;
  --paper-shade:#eef0f3;
  --backdrop:#2f3033;
  --photo-a:#8da3bd;
  --photo-b:#dfe6ee;
  --map:#d9dadc;
}
*{margin:0;padding:0;box-sizing:border-box}
html,body{width:1200px;height:776px;overflow:hidden;background:var(--backdrop)}
body{position:relative;font-family:"Questrial",sans-serif;color:var(--ink)}
.page{position:absolute;top:23px;width:560px;height:730px;background:linear-gradient(160deg,var(--paper) 40%,var(--paper-shade));overflow:hidden}
.page--front{left:30px}
.page--back{left:610px}
.abs{position:absolute}

/* front */
.brand{left:70px;top:52px;width:440px;font-family:"Playfair Display SC",serif;font-weight:700;font-size:31px;line-height:1.15;color:var(--ink);text-align:center}
.brand-rule{left:40px;top:150px;width:480px;height:4px;background:var(--blue)}
.photo{top:180px;height:150px;border:3px solid var(--blue);border-radius:20px}
.photo--tablet{left:45px;width:225px;background:linear-gradient(135deg,var(--photo-a),#3d4f66)}
.photo--notes{left:290px;width:225px;background:linear-gradient(135deg,var(--photo-b),#b6c6d8)}
.services{list-style:none;font-family:"Montserrat",sans-serif;font-weight:600;font-size:19px;line-height:1.35;color:var(--blue)}
.services li::before{content:"• ";}
.services--left{left:62px;top:360px}
.services--right{left:300px;top:345px}
.band{left:0;right:0;background:var(--blue);color:var(--paper)}
.band--front{top:470px;bottom:0;padding:34px 44px}
.body-text{font-size:13px;line-height:1.35}
.band-heading{font-family:"Montserrat",sans-serif;font-weight:600;font-size:14.5px;white-space:nowrap;margin:28px 0 14px}

/* back */
.band--back{top:0;height:300px;padding:30px 40px}
.band--back .band-heading{font-size:12.5px;margin:0 0 9px}
.band--back .body-text{font-size:10px;margin-bottom:11px}
.offer-title{left:40px;top:325px;font-family:"Montserrat",sans-serif;font-weight:600;font-size:16px;color:var(--blue)}
.offer-list{left:40px;top:352px;list-style:none;font-size:13px;line-height:1.35;color:var(--blue)}
.offer-list li::before{content:"•";display:inline-block;width:30px;color:var(--blue-dark)}
.callout{left:320px;top:322px;width:210px;font-family:"Montserrat",sans-serif;font-weight:600;font-size:11.5px;line-height:1.35;text-align:center;color:var(--blue)}
.contact{left:40px;top:500px;width:230px;text-align:center;font-size:15px;line-height:1.3;color:var(--blue-dark);font-style:normal}
.contact .web{margin-top:18px;display:block}
.map{left:290px;top:455px;width:240px;height:165px;border:3px solid var(--blue);border-radius:16px;background:linear-gradient(120deg,var(--map),#9fa2a7)}
</style>
</head>
<body>

<section class="page page--front">
  <h1 class="abs brand">Maplecrest Ambulatory<br>Surgery Center</h1>
  <div class="abs brand-rule"></div>

  <div class="abs photo photo--tablet" role="img" aria-label="Photo of a clinician reviewing a scan on a tablet"></div>
  <div class="abs photo photo--notes" role="img" aria-label="Photo of a doctor writing notes at a desk"></div>

  <ul class="abs services services--left">
    <li>ORTHOPEDICS</li>
    <li>PAIN MANAGEMENT</li>
    <li>PODIATRY</li>
  </ul>
  <ul class="abs services services--right">
    <li>OPHTHALMOLOGY</li>
    <li>ENT &amp; PEDIATRIC ENT</li>
    <li>GENERAL SURGERY</li>
  </ul>

  <div class="abs band band--front">
    <p class="body-text">Maplecrest Ambulatory Surgery Center, is a same day surgical center, conveniently located in Riverton, licensed by the state of New York and accredited by ACCB.</p>
    <h2 class="band-heading">CONVENIENT LOCATION FOR PATIENTS AND SURGEONS</h2>
    <p class="body-text">Maplecrest Ambulatory Surgery Center is conveniently located on Linden Avenue in Riverton, and is easily accessed from nearby towns and highways with ample parking available on site.</p>
  </div>
</section>

<section class="page page--back">
  <div class="abs band band--back">
    <h2 class="band-heading">CAPABILITIES OF MAPLECREST AMBULATORY SURGERY CENTER</h2>
    <p class="body-text">Maplecrest Ambulatory Surgery Center is a dedicated facility for same day procedures that do not require an overnight hospital stay, without sacrificing the quality of care and safety that a hospital provides. With over 15,000 sq ft of space and four operating rooms, the center offers specialties including orthopedics, pain management, podiatry, ophthalmology, ENT, pediatric ENT, and general surgery.</p>
    <p class="body-text">These same day procedures are performed by Maplecrest Ambulatory Surgery Center's highly skilled medical professionals that are committed to patient safety and satisfaction, providing the highest caliber of care with warmth and compassion in a personalized environment.</p>
    <h2 class="band-heading">BENEFITS OF CHOSING MAPLECREST AMBULATORY SURGERY CENTER</h2>
    <p class="body-text">More surgeons are choosing same day surgery centers because of the ability to provide high quality care in a state-of-the-art facility, at a more reasonable cost to you, your insurance provider, and your employer. Perhaps most importantly, same day surgery requires less down time, which means you'll spend less time away from your family and your job, and in most instances, you can return to your daily routine the next day.</p>
  </div>

  <h2 class="abs offer-title">WE OFFER</h2>
  <ul class="abs offer-list">
    <li>Orthopedics</li>
    <li>Pain Management</li>
    <li>Podiatry</li>
    <li>Ophthalmology</li>
    <li>Adult &amp; Pediatric ENT</li>
    <li>General Surgery</li>
  </ul>

  <p class="abs callout">Here at Maplecrest Ambulatory Surgery Center, the patient is our number one priority. To offer your patients the highest caliber care for same-day surgeries, contact Maplecrest Ambulatory Surgery Center today.</p>

  <address class="abs contact">
    2450 Linden Ave,<br>
    Riverton, NY 10999<br>
    Phone: (555) 014-2290<br>
    Email: info@medivantasc.com
    <span class="web">www.medivantasc.com</span>
  </address>

  <div class="abs map" role="img" aria-label="Street map marking the surgery center location"></div>
</section>

</body>
</html>
```